Business Card Design

I need a business card design for my law office based in Pasadena, California. I am a sole practitioner and I specialize in business transaction and litigation, probate and estate planning, taxation law, corporate and business formation, immigration and real estate. I want something that is simple, yet stands out.

A friend helped to create a logo about 6 years ago. I am open to new ideas to changing the logo.

Industry/Entity Type

Business

Contact Information for Business Card

Law Offices of Dorvan L. Mabry
842 W. Larkspur Ave., Suite 319
Pasadena, CA 90287
Tel: 626-555-0174
Fax: 626-555-0139
Email: dmabry@dlmlegalgroup.example

Attorney: Dorvan L. Mabry

```html
<!DOCTYPE html>
<html lang="en">
<head>
<meta charset="utf-8">
<title>Dorvan L. Mabry – Business Card</title>
<link rel="stylesheet" href="https://fonts.googleapis.com/css2?family=Cinzel:wght@400;500&family=Montserrat:wght@500;600;700&display=swap">
<style>
  :root {
    --backdrop: #e9eaec;
    --card: #a3ccd1;
    --ink: #1f2224;
    --paper-white: #ffffff;
    --card-w: 532px;
    --card-h: 329px;
  }
  * { box-sizing: border-box; margin: 0; padding: 0; }
  html, body {
    width: 1200px; height: 417px; overflow: hidden;
    background: var(--backdrop);
  }
  .canvas { position: relative; width: 1200px; height: 417px; }
  .card {
    position: absolute; top: 38px;
    width: var(--card-w); height: var(--card-h);
    background: var(--card);
    color: var(--ink);
  }
  .card--front { left: 17px; }
  .card--back { left: 644px; font-family: "Montserrat", sans-serif; }

  /* Front */
  .brand-mark {
    position: absolute; left: 0; right: 0; top: 112px;
    display: flex; align-items: center; justify-content: center; gap: 10px;
    font-family: "Cinzel", serif; font-weight: 500; font-size: 22px;
    letter-spacing: 0.06em; color: var(--ink);
  }
  .brand-mark__square { width: 14px; height: 14px; background: var(--ink); }
  .front-eyebrow {
    position: absolute; left: 0; right: 0; top: 190px;
    text-align: center;
    font-family: "Cinzel", serif; font-size: 10.5px; letter-spacing: 0.55em;
    text-transform: uppercase;
  }
  .front-rule {
    position: absolute; left: 124px; width: 284px; top: 210px;
    height: 1px; background: var(--ink);
  }
  .front-name {
    position: absolute; left: 0; right: 0; top: 218px;
    text-align: center;
    font-family: "Cinzel", serif; font-weight: 400; font-size: 36px;
    line-height: 1.1; letter-spacing: 0.01em;
  }

  /* Back */
  .back-mark {
    position: absolute; left: 45px; top: 47px;
    display: flex; align-items: center; gap: 7px;
    font-weight: 700; font-size: 12px; letter-spacing: 0.04em;
  }
  .back-mark__square { width: 10px; height: 10px; background: var(--ink); }
  .divider-dash {
    position: absolute; left: 45px; width: 16px; height: 2px;
    background: repeating-linear-gradient(to right, var(--paper-white) 0 7px, transparent 7px 9px);
  }
  .divider-dash--top { top: 145px; }
  .divider-dash--bottom { top: 248px; }
  .attorney-name {
    position: absolute; left: 45px; top: 164px;
    font-weight: 600; font-size: 15px;
  }
  .address {
    position: absolute; left: 45px; top: 182px;
    font-style: normal; font-weight: 500; font-size: 12px; line-height: 13.4px;
    letter-spacing: 0.03em; text-transform: uppercase; color: var(--paper-white);
  }
  .phones {
    position: absolute; left: 45px; top: 264px;
    font-weight: 600; font-size: 10px; line-height: 11.5px;
    letter-spacing: 0.04em; color: var(--paper-white);
  }
  .email {
    position: absolute; right: 67px; top: 275px;
    font-weight: 600; font-size: 10px; letter-spacing: 0.01em;
  }
</style>
</head>
<body>
<main class="canvas">
  <section class="card card--front" aria-label="Card front">
    <div class="brand-mark"><span class="brand-mark__square"></span>Mabry Law</div>
    <p class="front-eyebrow">Law Offices of</p>
    <div class="front-rule"></div>
    <h1 class="front-name">Dorvan L. Mabry</h1>
  </section>

  <section class="card card--back" aria-label="Card back">
    <div class="back-mark"><span class="back-mark__square"></span>Mabry Law</div>
    <div class="divider-dash divider-dash--top"></div>
    <h2 class="attorney-name">Attorney Dorvan L. Mabry</h2>
    <address class="address">
      842 W. Larkspur Ave.<br>
      Suite 319<br>
      Pasadena<br>
      CA 90287
    </address>
    <div class="divider-dash divider-dash--bottom"></div>
    <p class="phones">626 555 0174<br>626 555 0139</p>
    <p class="email">dmabry@dlmlegalgroup.example</p>
  </section>
</main>
</body>
</html>
```